8x8 Social Media Ad - Harbor Summit Expo

Attention Real Estate Agents
Please join us for our
Quarterly Real Estate Training Expo
The 2nd Saturday of February, May, August and November
Our Next Training Expo is _________________________________
From 9 am to 1 pm
at
Marlowe Suites Fernridge Station
4187 Copperleaf Lane, Greenbelt, MD 20770
Scheduled Speakers
9:00 am - Desmond Pryce - Orientation
9:30 am - Terrell Oakes - Multiple Income Streams / Keystone Track
10:00 am - Lorna Beckett - Marketing though Social Media
10:45 am - Raul Denning - Generating Business through Kelp-Nest
11:30 am - Tunde Adesemi - Real Estate Investing
12:15 pm - Marcus Oyelowo - (Main Speaker) Training Topic TBA
For more information call Desmond Pryce at (240) 555-0192 or email dpryce@harborsummithomes.example

```html
<!DOCTYPE html>
<html lang="en">
<head>
<meta charset="utf-8">
<title>Harbor Summit Expo – Quarterly Real Estate Training Expo</title>
<link rel="stylesheet" href="https://fonts.googleapis.com/css2?family=Fira+Sans:wght@400;500;600;700;800&family=Oswald:wght@600&display=swap">
<style>
  :root {
    --teal: #0f8f9e;
    --teal-bright: #1597a6;
    --black: #050505;
    --white: #ffffff;
    --mist: #ececec;
    --ink: #111111;
    --backdrop: #7b7b7b;
    --photo-a: #8d8f93;
    --photo-b: #4a4c52;
  }
  * { box-sizing: border-box; margin: 0; padding: 0; }
  html, body { width: 1200px; height: 904px; overflow: hidden; }
  body {
    background: var(--backdrop);
    font-family: "Fira Sans", Arial, sans-serif;
    position: relative;
  }
  .ad {
    position: absolute; left: 148px; top: 0;
    width: 904px; height: 904px;
    background: var(--black);
    overflow: hidden;
  }
  .info { position: absolute; left: 0; top: 0; width: 453px; height: 904px; }
  .brand {
    position: absolute; left: 0; top: 0; width: 453px; height: 214px;
    background: var(--white);
    display: flex; align-items: center; justify-content: center; gap: 14px;
  }
  .brand-mark { width: 46px; height: 46px; background: var(--teal); flex: none; }
  .brand-name {
    font-weight: 800; font-size: 23px; line-height: 1.15; color: var(--ink);
    letter-spacing: 0.5px; text-transform: uppercase;
  }
  .invite {
    position: absolute; left: 0; top: 214px; width: 453px; height: 179px;
    padding: 20px 0 0 45px;
  }
  .invite-lead { color: var(--white); font-weight: 800; font-size: 29px; letter-spacing: 0.3px; line-height: 34px; }
  .invite-title {
    font-family: "Oswald", "Arial Narrow", sans-serif; font-weight: 600;
    color: var(--teal-bright); font-size: 44px; line-height: 53px; margin-top: 2px;
  }
  .schedule {
    position: absolute; left: 0; top: 393px; width: 453px; height: 250px;
    background: linear-gradient(180deg, var(--white) 60%, #f3f3f3 100%);
    padding: 18px 0 0 47px;
  }
  .schedule-day { color: var(--teal-bright); font-weight: 800; font-size: 35px; line-height: 42px; }
  .schedule-months { color: var(--ink); font-weight: 600; font-size: 31px; line-height: 41px; }
  .schedule-next { color: var(--teal-bright); font-weight: 700; font-size: 24px; margin-top: 30px; }
  .schedule-blank { position: absolute; left: 45px; top: 238px; width: 336px; height: 2px; background: var(--ink); }
  .venue {
    position: absolute; left: 0; top: 643px; width: 453px; height: 141px;
    background: var(--mist); padding: 12px 0 0 45px;
  }
  .venue-time { font-weight: 700; font-size: 26px; color: var(--ink); line-height: 34px; }
  .venue-name { font-weight: 700; font-size: 20px; color: var(--teal-bright); margin-top: 4px; line-height: 26px; }
  .venue-address { font-weight: 500; font-size: 20px; color: var(--ink); line-height: 26px; }
  .contact { position: absolute; left: 45px; top: 800px; color: var(--white); font-size: 20px; line-height: 26.5px; }
  .contact-head { font-weight: 600; }
  .contact-label { color: var(--teal-bright); font-weight: 500; }
  .speakers { position: absolute; left: 462px; top: 0; width: 442px; height: 904px; background: var(--teal); }
  .speakers-head {
    position: absolute; left: 0; top: 22px; width: 442px; height: 50px; background: var(--black);
    color: var(--white); font-weight: 800; font-size: 28px; line-height: 50px; padding-left: 11px; letter-spacing: 0.3px;
  }
  .speaker { position: absolute; left: 11px; width: 431px; height: 124px; }
  .speaker-photo {
    position: absolute; left: 0; top: 0; width: 139px; height: 124px;
    background: linear-gradient(160deg, var(--photo-a), var(--photo-b));
  }
  .speaker-text { position: absolute; left: 163px; font-size: 20px; line-height: 26.5px; color: var(--white); }
  .speaker-name { color: var(--black); font-weight: 800; }
</style>
</head>
<body>
  <main class="ad">
    <section class="info">
      <header class="brand">
        <span class="brand-mark"></span>
        <span class="brand-name">Harbor Summit<br>Realty Group</span>
      </header>
      <div class="invite">
        <p class="invite-lead">PLEASE JOIN US FOR OUR</p>
        <h1 class="invite-title">Quarterly Real Estate<br>Training Expo</h1>
      </div>
      <div class="schedule">
        <p class="schedule-day">THE 2ND SATURDAY</p>
        <p class="schedule-months">of February, May, August<br>and November</p>
        <p class="schedule-next">OUR NEXT TRAINING EXPO IS</p>
        <span class="schedule-blank"></span>
      </div>
      <div class="venue">
        <p class="venue-time">From 9 am to 1 pm</p>
        <p class="venue-name">Marlowe Suites Fernridge Station</p>
        <p class="venue-address">4187 Copperleaf Lane,<br>Greenbelt, MD 20770</p>
      </div>
      <div class="contact">
        <p class="contact-head">FOR MORE INFORMATION</p>
        <p><span class="contact-label">call Desmond Pryce at</span> (240) 555-0192</p>
        <p><span class="contact-label">or email</span> dpryce@harborsummithomes.example</p>
      </div>
    </section>

    <section class="speakers">
      <h2 class="speakers-head">SCHEDULED SPEAKERS</h2>

      <article class="speaker" style="top:84px">
        <div class="speaker-photo" role="img" aria-label="Portrait photo of Desmond Pryce"></div>
        <p class="speaker-text" style="top:22px">9:00 am<br><span class="speaker-name">DESMOND PRYCE</span><br>Orientation</p>
      </article>
      <article class="speaker" style="top:219px">
        <div class="speaker-photo" role="img" aria-label="Portrait photo of Terrell Oakes"></div>
        <p class="speaker-text" style="top:8px">9:30 am<br><span class="speaker-name">TERRELL OAKES</span><br>Multiple Income Streams<br>/ Keystone Track</p>
      </article>
      <article class="speaker" style="top:355px">
        <div class="speaker-photo" role="img" aria-label="Portrait photo of Lorna Beckett"></div>
        <p class="speaker-text" style="top:8px">10:00 am<br><span class="speaker-name">LORNA BECKETT</span><br>Marketing though<br>Social Media</p>
      </article>
      <article class="speaker" style="top:490px">
        <div class="speaker-photo" role="img" aria-label="Portrait photo of Raul Denning"></div>
        <p class="speaker-text" style="top:8px">10:45 am<br><span class="speaker-name">RAUL DENNING</span><br>Generating Business<br>through Kelp-Nest</p>
      </article>
      <article class="speaker" style="top:625px">
        <div class="speaker-photo" role="img" aria-label="Portrait photo of Tunde Adesemi"></div>
        <p class="speaker-text" style="top:22px">11:30 am<br><span class="speaker-name">TUNDE ADESEMI</span><br>Real Estate Investing</p>
      </article>
      <article class="speaker" style="top:760px">
        <div class="speaker-photo" role="img" aria-label="Portrait photo of Marcus Oyelowo"></div>
        <p class="speaker-text" style="top:8px">12:15 pm<br><span class="speaker-name">MARCUS OYELOWO</span><br>(Main Speaker)<br>Training Topic TBA</p>
      </article>
    </section>
  </main>
</body>
</html>
```